Velvet Hounds Website - Boutique online pet store for both owners, their homes and their dogs

I need a high end online store for the sale of dog products (collars, leashes, coats etc), products for their owners (pyjamas, cosmetic bags, pencil cases, gift wrapping paper, greeting cards etc) and the owners home (ring holders, cushion covers, throws etc).

Please peruse the following website for a vauge idea of slightly similar stores:

Mybeaglecorner.example.com.au
Pawtrailhub.example.com.au
Terriertreats.example.com.au
Tallpup.example.co.za

Please keep in mind these are breed specific sites. I intend for the business to sell to trending dog breeds, for example, currently in Australia, French Bulldogs and Dachshunds are trending; therefore this will be the business's current focus.

I also intend for this website to be more elegant and refined than the websites mentioned above. Similar to top names brands, with a hint of cuteness to appeal to the animal lover within customers.

Target Market(s)

Velvet Hounds' target market is majority females, late 20's - 40's, either single, in a relationship, or with children who have left the home. They own small and pampered dogs and treat these dogs like their children. They will have a high disposable income.

I want the brand to attract elitist clientele. Comment has been made that people mightn't be able to spell Velvet when searching for the website; those are not the type of customers I want to attract. I think it may be difficult to encapsulate these two target ideas into the brand; I'd like is to appeal to both the 'Melbourne Socialite' and the Noosa stereotype of "I'm too cool to show it, but I really care what you think"

The products will be, for the most part, unique to the market, a few examples include:

custom hand made collars and leads reflecting current human fashion trends;
leather coats for dogs;
flannel pyjamas for dog;
chef's hats for dogs;
furniture which incorporates dogs beds (blanket box, coffee table, bedside table)
bags, cushions, throw rugs, pyjamas made from various dog print fabrics;
fine leather handbags and purses with various and discreet dog themed embellishments;
custom gift wrapping paper etc etc

Amazing customer service and high quality are two of the core values of Velvet Hounds.

The business will be run through the website as well as high-end markets around Brisbane, Gold Coast and Sunshine Coast.

Colors
eea4c8
ffffff
e34197

Requirements
Must have
• MUST BE FULLY OPERATIONAL ON COMPLETION. I own the domain name www.velvethounds.example.com.au. Needs to be functioning on this domain with an operational online store using PayPal.
• Must also be mobile friendly.
• Pages:
• For your pup (shopping page)
• For your home (shopping page)
• For you (shopping page)
• Stationery
• Contact us
• I am open to better and more creative page names.
• MUST have an easy to operate back end that I can use to update products as and when required.

```html
<!DOCTYPE html>
<html lang="en">
<head>
<meta charset="utf-8">
<title>Velvet Hounds — Slippers</title>
<link rel="stylesheet" href="https://fonts.googleapis.com/css2?family=Arimo:ital,wght@0,400;0,700;1,400&family=PT+Sans:wght@400;700&family=Tinos&display=swap">
<style>
  :root {
    --pink-soft: #eea4c8;
    --pink-strong: #e34197;
    --white: #ffffff;
    --page-bg: #e6e6e6;
    --column-bg: #ececec;
    --ink: #111111;
    --body-ink: #5a607a;
    --rule: #b9b9b9;
    --mint: #b8dfe0;
    --mint-ink: #8a9a9b;
    --footer-dark: #222222;
    --footer-black: #000000;
    --pale-strip: #f3f3f3;
  }
  * { box-sizing: border-box; margin: 0; padding: 0; }
  html, body { width: 1081px; height: 1200px; overflow: hidden; }
  body {
    position: relative;
    background: radial-gradient(ellipse at 50% 0%, #f7f7f7 0%, var(--page-bg) 60%);
    font-family: "Arimo", Arial, sans-serif;
    color: var(--ink);
  }
  .abs { position: absolute; }

  .page-column {
    left: 120px; top: 0; width: 846px; height: 1200px;
    background: var(--column-bg);
    box-shadow: 0 0 6px rgba(150,170,190,.45);
  }
  .side-band { top: 115px; height: 39px; background: var(--pink-soft); }
  .side-band.left { left: 0; width: 120px; }
  .side-band.right { left: 966px; width: 115px; }

  .brand {
    left: 120px; width: 846px; top: 40px;
    display: flex; justify-content: center; align-items: center; gap: 12px;
  }
  .brand-mark { width: 30px; height: 30px; background: var(--pink-strong); }
  .brand-name {
    font-family: "PT Sans", sans-serif; font-weight: 700; font-size: 30px;
    letter-spacing: 3px; color: var(--pink-strong);
  }

  .main-nav {
    left: 120px; top: 138px; width: 846px; height: 38px;
    background: var(--pink-soft);
    font-size: 14.5px; text-transform: uppercase;
  }
  .main-nav span { position: absolute; top: 11px; }
  .main-nav .current { color: var(--white); }
  .cart-icon { position: absolute; left: 770px; top: 10px; }

  .rule { height: 2px; background: var(--rule); border-bottom: 1px solid #f8f8f8; }

  .product-photo {
    left: 151px; top: 250px; width: 292px; height: 291px;
    background: var(--white); border: 1px solid #d3d3d3; padding: 14px;
  }
  .product-photo .fill {
    width: 100%; height: 100%;
    background: radial-gradient(ellipse at 50% 50%, #e3a8a6 0%, #d99995 45%, #ffffff 80%);
  }

  .product-title {
    left: 563px; top: 253px; font-family: "PT Sans", sans-serif;
    font-weight: 700; font-size: 21px; color: var(--body-ink);
  }
  .product-price {
    left: 820px; top: 240px; font-family: "PT Sans", sans-serif;
    font-weight: 700; font-size: 33px; color: var(--pink-strong);
  }
  .product-copy {
    left: 563px; top: 292px; width: 350px;
    font-family: "PT Sans", sans-serif; font-size: 14.2px; line-height: 22px;
    color: var(--body-ink);
  }
  .select-box {
    left: 564px; width: 130px; height: 23px;
    border: 1px solid #d6d6d6; border-radius: 2px;
    background: linear-gradient(#fdfdfd, #e8e8e8);
    font-size: 10px; color: var(--body-ink); padding: 5px 6px;
  }
  .select-box::after {
    content: "▴\A▾"; white-space: pre; position: absolute; right: 0; top: 0;
    width: 13px; height: 21px; border-left: 1px solid #d6d6d6;
    font-size: 6px; line-height: 8px; text-align: center; padding-top: 3px; color: #444;
  }
  .btn {
    top: 634px; height: 20px; font-style: italic; font-size: 10px;
    display: flex; align-items: center; justify-content: center;
  }
  .btn-cart { left: 563px; width: 105px; background: var(--pink-strong); color: var(--white); }
  .btn-wish { left: 673px; width: 107px; background: var(--mint); color: var(--mint-ink); }

  .similar-tab {
    left: 151px; top: 714px; width: 156px; height: 30px;
    background: var(--pink-strong); color: var(--white);
    font-size: 14.5px; display: flex; align-items: center; justify-content: center;
  }
  .item-card { top: 768px; width: 156px; }
  .item-card .thumb {
    height: 155px; background: var(--white); border: 1px solid #d3d3d3; padding: 22px 14px;
  }
  .item-card .thumb .fill {
    width: 100%; height: 100%;
    background: radial-gradient(ellipse, #3b3b45 0%, #2a2a32 55%, #ffffff 85%);
  }
  .item-card .caption {
    display: flex; justify-content: space-between; margin-top: 10px; font-size: 13.5px;
  }
  .item-card .name { color: var(--body-ink); }
  .item-card .price { color: var(--pink-strong); }

  .pale-strip { left: 0; top: 966px; width: 1081px; height: 40px; background: var(--pale-strip); }
  .footer-black { left: 0; top: 1006px; width: 1081px; height: 194px; background: var(--footer-black); }
  .footer-column { left: 120px; top: 966px; width: 846px; height: 234px; background: var(--footer-dark); }
  .footer-band { left: 120px; top: 982px; width: 846px; height: 32px; background: var(--pink-soft); }
  .footer-heading { top: 1031px; font-size: 13px; font-weight: 700; color: var(--pink-strong); }
  .footer-heading.social { color: var(--white); font-weight: 400; }
  .footer-list { top: 1053px; list-style: none; font-size: 13px; line-height: 16.4px; color: var(--white); }
  .social-dot { top: 1065px; width: 38px; height: 38px; border-radius: 50%; background: var(--white); }
  .copyright {
    left: 120px; width: 846px; top: 1165px; text-align: center;
    font-family: "Tinos", serif; font-size: 9.5px; color: var(--white);
  }
</style>
</head>
<body>
  <div class="abs page-column"></div>
  <div class="abs side-band left"></div>
  <div class="abs side-band right"></div>

  <header class="abs brand">
    <span class="brand-mark"></span>
    <span class="brand-name">VELVET HOUNDS</span>
  </header>

  <nav class="abs main-nav">
    <span class="current" style="left:22px">Home</span>
    <span style="left:86px">Puppies</span>
    <span style="left:168px">Mens</span>
    <span style="left:230px">Womens</span>
    <span style="left:316px">Stationery</span>
    <span style="left:420px">Contact Us</span>
    <span style="left:601px">Cart</span>
    <svg class="cart-icon" width="18" height="17" viewBox="0 0 18 17" aria-hidden="true">
      <path d="M1 2h3l2 9h9l2-6H5" fill="none" stroke="#fff" stroke-width="1.6"/>
      <circle cx="7.5" cy="14.5" r="1.5" fill="#fff"/>
      <circle cx="13.5" cy="14.5" r="1.5" fill="#fff"/>
    </svg>
    <span style="left:702px">Login | Signup</span>
  </nav>

  <div class="abs rule" style="left:142px; top:211px; width:824px;"></div>

  <div class="abs product-photo">
    <div class="fill" role="img" aria-label="Product photo: pink slippers with a dark dachshund silhouette"></div>
  </div>

  <h1 class="abs product-title">Slippers</h1>
  <div class="abs product-price">$8.50</div>
  <p class="abs product-copy">Lorem ipsum dolor sit amet, consectetur adipiscing elit. Nullam venenatis cursus gravida. Suspendisse ut ligula tristique velit blandit vel sit amet ipsum. Nam accumsan turpis id mauris fermentum pharetra. Cras interdum, risus et dictum bibendum, arcu tellus convallis libero, quis placerat urna erat et lorem. Phasellus inter dum turpis vestibulum ligula varius sit amet ultricies massa vulputate. Morbis vehicula, velit a faucibus cursus, turpis magna mattis mi, in ultrices tortor nibh eu dui. Nam at ipsum in urna convallis accumsan. Nullam at</p>

  <div class="abs select-box" style="top:546px">Select Size</div>
  <div class="abs select-box" style="top:581px">Select Qty.</div>

  <div class="abs btn btn-cart">Add to Cart</div>
  <div class="abs btn btn-wish">Add to Wishlist</div>

  <div class="abs rule" style="left:132px; top:728px; width:822px;"></div>
  <div class="abs similar-tab">SIMILAR ITEMS</div>

  <div class="abs item-card" style="left:138px">
    <div class="thumb"><div class="fill" role="img" aria-label="Product photo: dark purse with white dachshund print"></div></div>
    <div class="caption"><span class="name">Purse</span><span class="price">$9.50</span></div>
  </div>
  <div class="abs item-card" style="left:354px">
    <div class="thumb"><div class="fill" role="img" aria-label="Product photo: dark purse with white dachshund print"></div></div>
    <div class="caption"><span class="name">Purse</span><span class="price">$9.50</span></div>
  </div>
  <div class="abs item-card" style="left:569px">
    <div class="thumb"><div class="fill" role="img" aria-label="Product photo: dark purse with white dachshund print"></div></div>
    <div class="caption"><span class="name">Purse</span><span class="price">$9.50</span></div>
  </div>
  <div class="abs item-card" style="left:784px">
    <div class="thumb"><div class="fill" role="img" aria-label="Product photo: dark purse with white dachshund print"></div></div>
    <div class="caption"><span class="name">Purse</span><span class="price">$9.50</span></div>
  </div>

  <div class="abs pale-strip"></div>
  <div class="abs footer-black"></div>
  <footer>
    <div class="abs footer-column"></div>
    <div class="abs footer-band"></div>

    <h2 class="abs footer-heading" style="left:142px">LINKS</h2>
    <ul class="abs footer-list" style="left:142px">
      <li>Home</li><li>Mens</li><li>Womens</li><li>Stationary</li><li>Contact Us</li>
    </ul>

    <h2 class="abs footer-heading" style="left:509px">ON SALE ITEMS</h2>
    <ul class="abs footer-list" style="left:518px">
      <li>Lorem ipsum</li><li>Lorem Ipsum</li><li>Lorem Ipsum</li><li>Lorem Ipsum</li>
    </ul>

    <h2 class="abs footer-heading social" style="left:789px">GET SOCIAL WITH US!</h2>
    <span class="abs social-dot" style="left:791px" aria-label="Social link"></span>
    <span class="abs social-dot" style="left:845px" aria-label="Social link"></span>
    <span class="abs social-dot" style="left:898px" aria-label="Social link"></span>

    <p class="abs copyright">© Copyright © 2011. Company name all rights reserved.</p>
  </footer>
</body>
</html>
```